Business Card for plovrix

Create a Business Card with an existing logo for plovrix AG. We are a Information Technology company that does consulting and developing SW to automate business processes. The main colors are given from the logo.

Industry/Entity Type

Business

Requirements
Nice to have
• we use a a font style Century Gothic in our documents

```html
<!DOCTYPE html>
<html lang="en">
<head>
<meta charset="utf-8">
<title>plovrix AG – Business Card</title>
<link href="https://fonts.googleapis.com/css2?family=Didact+Gothic&family=Mulish:wght@400;700&display=swap" rel="stylesheet">
<style>
  :root{
    --page:#ece9e4;
    --blue-deep:#1736a0;
    --blue-mid:#1560c8;
    --blue-bright:#1fa3e3;
    --green:#7cc82a;
    --green-light:#b7e04a;
    --white:#ffffff;
    --ink:#3a3d44;
    --steel-light:#c9d3ea;
    --steel:#8fa3d3;
  }
  *{box-sizing:border-box;margin:0;padding:0}
  html,body{width:1200px;height:1024px;overflow:hidden;background:var(--page)}
  .sheet{position:relative;width:1200px;height:1024px}
  .card{position:absolute;left:200px;width:800px;height:457px;border-radius:28px;overflow:hidden;
        box-shadow:0 10px 28px rgba(0,0,0,.18)}
  .card--front{top:36px}
  .card--back{top:531px}
  .card svg.card-art{position:absolute;inset:0;width:100%;height:100%}

  .back-field{position:absolute;inset:0;
    background:
      radial-gradient(ellipse 60% 70% at 25% 25%, rgba(31,163,227,.85), rgba(31,163,227,0) 70%),
      radial-gradient(ellipse 60% 70% at 85% 85%, rgba(124,200,42,.75), rgba(124,200,42,0) 70%),
      linear-gradient(135deg, var(--blue-mid) 0%, var(--steel) 55%, var(--steel-light) 100%);}

  .brand{position:absolute;display:flex;align-items:center;gap:18px;
         font-family:"Didact Gothic",sans-serif;color:var(--ink);letter-spacing:-1px}
  .brand__dot{border-radius:50%;background:var(--blue-mid)}
  .brand--front{left:70px;top:180px;font-size:78px}
  .brand--front .brand__dot{width:54px;height:54px}
  .brand--back{left:260px;top:170px;font-size:84px;color:var(--white)}
  .brand--back .brand__dot{width:58px;height:58px;background:var(--green)}

  .contact{position:absolute;right:42px;top:48px;text-align:right;color:var(--white);
           font-family:"Mulish",sans-serif;font-size:17px;line-height:1.5}
  .contact__name{font-weight:700;font-size:27px;line-height:1.1}
  .contact__role{color:var(--green-light);font-weight:700;font-size:19px;margin-bottom:14px}
  .contact__line{display:flex;justify-content:flex-end;align-items:center;gap:8px}
  .contact__icon{width:14px;height:14px;flex:none}
  .contact__address{margin-top:22px}

  .back-web{position:absolute;left:36px;top:250px;transform:rotate(-90deg);transform-origin:left top;
            font-family:"Mulish",sans-serif;font-size:14px;color:var(--white);letter-spacing:.5px}
</style>
</head>
<body>
<div class="sheet">

  <section class="card card--front" aria-label="Business card front">
    <svg class="card-art" viewBox="0 0 800 457" preserveAspectRatio="none" aria-hidden="true">
      <defs>
        <linearGradient id="frontBlue" x1="0" y1="0" x2="1" y2="1">
          <stop offset="0" stop-color="var(--blue-deep)"/>
          <stop offset=".5" stop-color="var(--blue-bright)"/>
          <stop offset="1" stop-color="var(--blue-deep)"/>
        </linearGradient>
        <linearGradient id="frontWhite" x1="0" y1="0" x2="1" y2="0">
          <stop offset="0" stop-color="#ffffff"/>
          <stop offset="1" stop-color="#eef2ee"/>
        </linearGradient>
      </defs>
      <rect width="800" height="457" fill="url(#frontBlue)"/>
      <path d="M0,0 H440 C380,110 360,260 470,457 H0 Z" fill="var(--green)"/>
      <path d="M0,0 H418 C352,120 340,270 448,457 H0 Z" fill="url(#frontWhite)"/>
      <path d="M0,360 C140,300 300,330 448,457 H0 Z" fill="#e4e9f2" opacity=".7"/>
    </svg>

    <div class="brand brand--front"><span class="brand__dot"></span>plovrix</div>

    <div class="contact">
      <div class="contact__name">Jonas Keller</div>
      <div class="contact__role">CEO</div>
      <div class="contact__line">+41 56 210 48 37
        <svg class="contact__icon" viewBox="0 0 14 14" aria-hidden="true"><circle cx="7" cy="7" r="7" fill="var(--green)"/><path d="M4.5 3.5l1.5 1.5-1 1c.6 1.2 1.5 2.1 2.7 2.7l1-1 1.5 1.5-1 1.2C6.5 10 4 7.5 3.5 4.7z" fill="#fff"/></svg></div>
      <div class="contact__line">+41 79 635 90 24
        <svg class="contact__icon" viewBox="0 0 14 14" aria-hidden="true"><circle cx="7" cy="7" r="7" fill="var(--green)"/><rect x="5" y="3" width="4" height="8" rx="1" fill="#fff"/></svg></div>
      <div class="contact__line">www.plovrix.ch
        <svg class="contact__icon" viewBox="0 0 14 14" aria-hidden="true"><circle cx="7" cy="7" r="7" fill="var(--green)"/><circle cx="7" cy="7" r="3.5" fill="none" stroke="#fff" stroke-width="1.2"/></svg></div>
      <div class="contact__line">jonas.keller@plovrix.ch
        <svg class="contact__icon" viewBox="0 0 14 14" aria-hidden="true"><circle cx="7" cy="7" r="7" fill="var(--green)"/><rect x="3.5" y="4.5" width="7" height="5" fill="none" stroke="#fff" stroke-width="1.1"/><path d="M3.5 4.5l3.5 3 3.5-3" fill="none" stroke="#fff" stroke-width="1.1"/></svg></div>
      <div class="contact__address">Lindenweg 7,<br>5430 Wettingen, Switzerland</div>
    </div>
  </section>

  <section class="card card--back" aria-label="Business card back">
    <div class="back-field" role="img" aria-label="Decorative flowing blue and green wave background"></div>
    <div class="brand brand--back">plovrix<span class="brand__dot"></span></div>
    <div class="back-web">www.plovrix.ch</div>
  </section>

</div>
</body>
</html>
```